Commercial Real Estate Executive Recruiting Firm Needs Business Card Design

We need a business card design for MARLOW | Executive Recruiting - an executive recruiting firm focused exclusively on the commercial real estate industry. We place professionals ranging from Analyst to the Executive Office covering all investment/finance disciplines (acquisitions, asset management, capital markets, etc.) in all product types (office, retail, multifamily, industrial, land, etc.). We have a passion for helping people (clients and candidates) and have a reputation for being open and honest in our recruiting - and yes, very successful. We have recently developed a new logo and would like to update our business cards as well. I've uploaded some information about our company that contains the new logo.

Target Market(s)

Commercial Real Estate professionals. Primarily in the US. These are typically, smart, driven professionals with finance degrees and MBAs. Primarily men between the ages of 25 and 55.

Industry/Entity Type

Real Estate

Font styles to use
Other font styles liked:
• The font for "MARLOW" is Blair ITC (Medium), and "executive recruiting" is Gotham (Book).

Requirements
Must have
• I like the idea of white background on one side and solid color (blue, black, etc.) on back of card.

Would like to utilize the fonts in the logo (to the extent possible) so as to not have too many fonts on card.
Nice to have
• I think the roles (i.e., Acquisitions, Asset Management, etc.,...) is probably likely best placed on the back side of the card with the logo maybe. See attached current business card for content.

```html
<!DOCTYPE html>
<html lang="en">
<head>
<meta charset="utf-8">
<title>MARLOW | Executive Recruiting — Business Card</title>
<link rel="stylesheet" href="https://fonts.googleapis.com/css2?family=Montserrat:ital,wght@0,300;0,400;0,500;1,400&display=swap">
<style>
  :root {
    --stage: #58585a;
    --card-white: #ececee;
    --brand-blue: #2c6aa0;
    --brand-blue-deep: #245c8e;
    --logo-blue: #3a86c8;
    --ink: #4a4a4c;
    --ink-soft: #8a8a8e;
    --paper: #ffffff;
  }
  * { box-sizing: border-box; margin: 0; padding: 0; }
  html, body {
    width: 1200px; height: 1000px; overflow: hidden;
    background: var(--stage);
    font-family: "Montserrat", Arial, sans-serif;
  }
  .card-set {
    position: absolute; inset: 0;
    display: flex; justify-content: center; align-items: center; gap: 80px;
  }
  .card {
    position: relative; width: 360px; height: 620px;
    box-shadow: 0 8px 24px rgba(0,0,0,.35);
    overflow: hidden;
  }

  /* Front */
  .card-front { background: var(--card-white); color: var(--ink); }
  .brand {
    position: absolute; top: 58px; left: 40px;
    display: flex; align-items: center; gap: 14px;
  }
  .brand-square { width: 34px; height: 34px; background: var(--logo-blue); }
  .brand-rule { width: 1px; height: 40px; background: var(--ink-soft); }
  .brand-name {
    font-size: 30px; font-weight: 400; letter-spacing: 10px; color: var(--ink);
    line-height: 1;
  }
  .brand-tagline {
    font-size: 12px; font-weight: 400; letter-spacing: 3.4px; color: var(--ink-soft);
    margin-top: 4px;
  }
  .person { position: absolute; top: 250px; width: 100%; text-align: center; }
  .person-name { font-size: 36px; font-weight: 400; letter-spacing: .5px; }
  .person-title { font-size: 11px; letter-spacing: 5px; color: var(--ink-soft); margin-top: 2px; }
  .phone {
    position: absolute; top: 400px; width: 100%; text-align: center;
    font-size: 19px; letter-spacing: 2px;
  }
  .contact-band {
    position: absolute; left: 0; right: 0; bottom: 0; height: 108px;
    background: var(--brand-blue); color: var(--paper);
    display: flex; flex-direction: column; justify-content: center; align-items: center; gap: 6px;
    font-size: 17px; letter-spacing: 1.6px;
  }

  /* Back */
  .card-back {
    background: radial-gradient(circle at 50% 50%, #ffffff 0%, #ffffff 18%, #c7d8ea 32%, #5d90c0 46%, var(--brand-blue) 60%);
    color: var(--paper); text-align: center;
  }
  .back-heading { position: absolute; top: 30px; width: 100%; font-size: 20px; font-weight: 400; }
  .back-sub { position: absolute; top: 62px; width: 100%; font-size: 12.5px; font-style: italic; }
  .back-mark {
    position: absolute; top: 50%; left: 50%; transform: translate(-50%, -50%);
    display: flex; flex-direction: column; align-items: center; gap: 14px;
  }
  .back-mark-square { width: 90px; height: 90px; background: var(--logo-blue); }
  .back-mark-name { font-size: 26px; font-weight: 400; letter-spacing: 9px; color: var(--brand-blue-deep); }
  .disciplines {
    position: absolute; bottom: 24px; right: 14px; text-align: right;
    font-size: 15px; line-height: 1.35;
  }
</style>
</head>
<body>
  <main class="card-set">
    <section class="card card-front" aria-label="Card front">
      <div class="brand">
        <div class="brand-square"></div>
        <div class="brand-rule"></div>
        <div>
          <div class="brand-name">MARLOW</div>
          <div class="brand-tagline">executive recruiting</div>
        </div>
      </div>
      <div class="person">
        <div class="person-name">Jordan Hale</div>
        <div class="person-title">PRESIDENT</div>
      </div>
      <div class="phone">M | 312-555-0147</div>
      <div class="contact-band">
        <span>jordan@marlowrecruiting.com</span>
        <span>www.marlowrecruiting.com</span>
      </div>
    </section>

    <section class="card card-back" aria-label="Card back">
      <h1 class="back-heading">Comercial Real Estate Recruiting</h1>
      <p class="back-sub">Analyst to Executive Office Placement</p>
      <div class="back-mark">
        <div class="back-mark-square"></div>
        <div class="back-mark-name">MARLOW</div>
      </div>
      <p class="disciplines">Asset Management | Banking<br>Capital Markets | Brokerage</p>
    </section>
  </main>
</body>
</html>
```